Lawn & Garden Maintenace Business card design needed

I need a basic business card design for a Lawn Mowing & Garden Maintenance business

I would like it to look a combination of classy, striking, with vibrant Green/s, I will attached a very rough idea of what I would like but I am open to new suggestions, and the possibility of doing it on a darker charcoal or black gloss card, please don't just send me a version of what I've attached it's a very rough idea & more based around the text layout than anything else, feel free to let your creative instincts fly!

Must have grass across the bottom of the Card & i would prefer it to be portrait rather than landscape.

I quite like the coloring of this previously submitted card
http://www.artspark-example.com/design/2840613

Please have the text in White and Green if you are submitting a dark card, thank you.

Business

R.K. Lawn & Garden Services

Free Quote - Great Rates

Rob Kessler
0417 362 918
Info@RKLawnAndGarden.example.au

Requirements
Must have
• Must have grass across bottom of card preferably photo real grass rather than illustrated.
Nice to have
• Small telephone icon for phone number small email icon for email address but only if both icon are similar size and don't take away from the overall look of the card

Would also be nice to a have a flow/style that would be easily transferable to flyers & advertising

```html
<!DOCTYPE html>
<html lang="en">
<head>
<meta charset="utf-8">
<title>R.K. Lawn &amp; Garden Services – Business Card</title>
<link rel="stylesheet" href="https://fonts.googleapis.com/css2?family=Arimo:wght@400;700&family=Tinos&display=swap">
<style>
  :root {
    --page-bg: #dcdcdc;
    --card-top: #2a2a2a;
    --card-bottom: #050505;
    --brand-green: #6dbb2c;
    --bright-green: #8fd42e;
    --text-white: #ffffff;
    --pill-bg: #0b0b0b;
    --pill-edge: #2c2c2c;
    --grass-light: #a6e03a;
    --grass-mid: #4fa01c;
    --grass-dark: #123a08;
  }
  * { margin: 0; padding: 0; box-sizing: border-box; }
  html, body {
    width: 1200px;
    height: 861px;
    overflow: hidden;
    background: var(--page-bg);
  }
  .canvas {
    position: relative;
    width: 1200px;
    height: 861px;
  }
  .business-card {
    position: absolute;
    left: 435px;
    top: 120px;
    width: 330px;
    height: 620px;
    background: linear-gradient(160deg, var(--card-top) 0%, #111 45%, var(--card-bottom) 100%);
    overflow: hidden;
    box-shadow: 0 10px 30px rgba(0,0,0,.35);
  }
  .business-name {
    position: absolute;
    top: 70px;
    left: 30px;
    width: 270px;
    text-align: center;
    font-family: "Tinos", "Times New Roman", serif;
    font-weight: 400;
    font-size: 30px;
    line-height: 1.2;
    color: var(--brand-green);
  }
  .person-name {
    position: absolute;
    top: 222px;
    width: 100%;
    text-align: center;
    font-family: "Tinos", "Times New Roman", serif;
    font-size: 44px;
    color: var(--text-white);
  }
  .contact-pill {
    position: absolute;
    left: 50%;
    transform: translateX(-50%);
    display: flex;
    align-items: center;
    gap: 8px;
    height: 26px;
    padding: 0 8px;
    background: var(--pill-bg);
    border: 1px solid var(--pill-edge);
    border-radius: 6px;
    font-family: "Arimo", Arial, sans-serif;
    font-size: 13px;
    color: var(--text-white);
    white-space: nowrap;
  }
  .contact-phone { top: 290px; }
  .contact-email { top: 327px; }
  .contact-pill svg { display: block; fill: var(--brand-green); }
  .offer-headline {
    position: absolute;
    top: 412px;
    width: 100%;
    text-align: center;
    font-family: "Arimo", Arial, sans-serif;
    font-weight: 700;
    font-size: 19px;
    color: var(--brand-green);
  }
  .service-list {
    position: absolute;
    top: 437px;
    width: 100%;
    text-align: center;
    font-family: "Arimo", Arial, sans-serif;
    font-size: 10.5px;
    color: var(--text-white);
  }
  .grass-band {
    position: absolute;
    left: 0;
    bottom: 0;
    width: 100%;
    height: 125px;
    background:
      radial-gradient(ellipse at 55% 35%, rgba(166,224,58,.85) 0%, rgba(166,224,58,0) 60%),
      linear-gradient(to bottom, rgba(0,0,0,0) 0%, var(--grass-mid) 25%, var(--bright-green) 45%, var(--grass-mid) 75%, var(--grass-dark) 100%);
  }
</style>
</head>
<body>
<main class="canvas">
  <section class="business-card">
    <h1 class="business-name">R.K. Lawn &amp; Garden Services</h1>

    <p class="person-name">Rob Kessler</p>

    <p class="contact-pill contact-phone">
      <svg width="9" height="15" viewBox="0 0 9 15" aria-hidden="true"><rect x="0" y="2" width="9" height="13" rx="1.5"/><rect x="6" y="0" width="1.5" height="3"/><rect x="2" y="4" width="5" height="3" fill="#0b0b0b"/></svg>
      <span>0417 362 918</span>
      <svg width="9" height="15" viewBox="0 0 9 15" aria-hidden="true"><rect x="0" y="2" width="9" height="13" rx="1.5"/><rect x="6" y="0" width="1.5" height="3"/><rect x="2" y="4" width="5" height="3" fill="#0b0b0b"/></svg>
    </p>

    <p class="contact-pill contact-email">
      <svg width="16" height="11" viewBox="0 0 16 11" aria-hidden="true"><rect width="16" height="11" rx="1"/><path d="M1 1 L8 6.5 L15 1" stroke="#0b0b0b" stroke-width="1.3" fill="none"/></svg>
      <span>Info@RKLawnAndGarden.example.au</span>
      <svg width="16" height="11" viewBox="0 0 16 11" aria-hidden="true"><rect width="16" height="11" rx="1"/><path d="M1 1 L8 6.5 L15 1" stroke="#0b0b0b" stroke-width="1.3" fill="none"/></svg>
    </p>

    <p class="offer-headline">FREE QUOTE - GREAT RATES</p>
    <p class="service-list">Mowing • Edging • Trimming • Weeding • Planting &amp; More</p>

    <div class="grass-band" role="img" aria-label="Photo of bright green lawn grass across the bottom of the card"></div>
  </section>
</main>
</body>
</html>
```